Informational Site for Advanced Chemistry R&D

The company develops oxidation chemistry for air, water, fuel pollution controls. The site has been prototyped at www.velmirlab.net. Take a look. Now, the task is to design it for eye-catching beauty with use of color, on-page scroll-driven color transition and parallax effects. Should capture the themes: high technology, wow it's beautiful, modern, uncluttered, clean urban environment.

Target Market(s)

China Environmentally Conscious Government and Industry,

Industry/Entity Type

It Company

Number of Pages Required

3 page

Font styles to use
Sans Serif

Requirements
Must have
• Parallax effects, desktop compatible, Rich, Modern, Simple, Graphic
Nice to have
• Mobile Phone Compatible
Should not have
• Flash, or anything that is slow to load or requires high bandwidth

```html
<!DOCTYPE html>
<html lang="en">
<head>
<meta charset="utf-8">
<title>VelmirLab — Advanced Oxidation Science</title>
<link rel="stylesheet" href="https://fonts.googleapis.com/css2?family=Questrial&family=Raleway:wght@500;600&family=Open+Sans:wght@400;600;700&display=swap">
<style>
:root{
  --ink:#1a1a1a;
  --topbar:#242424;
  --blue:#1a6fb8;
  --blue-dark:#145c9c;
  --teal:#2ebab6;
  --teal-light:#3cc6c0;
  --grey-band:#e8e8e8;
  --label-bg:#e2dcd8;
  --text-grey:#555;
  --white:#fff;
}
*{box-sizing:border-box;margin:0;padding:0}
html,body{width:729px;height:1200px;overflow:hidden}
body{font-family:"Open Sans",sans-serif;color:var(--ink);background:var(--white);position:relative}

.hero{position:absolute;left:0;top:0;width:729px;height:448px;
  background:linear-gradient(180deg,#2c2e30 0%,#3a3b3a 45%,#2f2a25 75%,#3a3026 100%)}
.hero-top{position:absolute;left:0;top:0;width:729px;height:90px;background:var(--topbar)}
.hero-top .email{position:absolute;left:93px;top:29px;font-size:8px;color:#9a9a9a}
.hero-top .phone{position:absolute;left:500px;top:27px;font-size:8px;color:#9a9a9a}
.brand{position:absolute;left:0;width:729px;top:18px;text-align:center;display:flex;flex-direction:column;align-items:center;gap:3px}
.brand .dot{width:22px;height:22px;border-radius:50%;background:var(--blue)}
.brand .name{font-family:"Raleway",sans-serif;font-weight:600;font-size:12px;color:var(--blue);letter-spacing:.2px}

.nav{position:absolute;left:28px;top:65px;width:671px;height:53px;background:var(--blue);border-radius:3px;display:flex;padding-left:90px}
.nav a{display:flex;align-items:center;justify-content:center;height:53px;font-size:8.5px;font-weight:700;color:var(--white);text-decoration:none;letter-spacing:.3px}
.nav a.home{width:77px;background:var(--teal);border:1px solid #9ee4e1}
.nav a.about{width:95px}
.nav a.tech{width:106px}
.nav a.prod{width:100px}
.nav a.contact{width:102px}

.hero-photo{position:absolute;left:0;top:90px;width:729px;height:358px}
.hero-title{position:absolute;left:0;top:194px;width:729px;text-align:center;font-family:"Questrial",sans-serif;font-size:34px;line-height:41px;color:var(--white)}
.hero-sub{position:absolute;left:0;top:330px;width:729px;text-align:center;font-family:"Raleway",sans-serif;font-weight:500;font-size:12px;color:var(--teal-light)}
.btn{display:inline-flex;align-items:center;justify-content:center;font-size:6.5px;font-weight:600;color:var(--white);background:var(--blue);text-transform:uppercase;border-radius:2px}
.hero .btn{position:absolute;left:323px;top:354px;width:83px;height:25px;border:1px solid #cfe3f5;border-radius:4px}
.slider-ctrl{position:absolute;left:348px;top:430px;width:39px;height:18px;background:#f0f0f0;display:flex;align-items:center;justify-content:center;gap:8px}

.welcome{position:absolute;left:0;top:448px;width:729px;height:177px;background:var(--grey-band);text-align:center}
.welcome h2{position:absolute;left:0;top:29px;width:729px;font-family:"Questrial",sans-serif;font-weight:400;font-size:22px;color:#111}
.welcome h2 span{color:var(--blue)}
.welcome .rule{position:absolute;top:41px;height:1px;width:177px;background:#bdbdbd}
.welcome .rule.l{left:28px}.welcome .rule.r{left:522px}
.welcome p{position:absolute;left:78px;top:69px;width:573px;font-size:6.6px;line-height:13.5px;color:var(--text-grey)}
.welcome .btn{position:absolute;left:325px;top:124px;width:79px;height:24px}

.solutions{position:absolute;left:0;top:625px;width:729px;height:331px;background:var(--white)}
.solutions h2{position:absolute;left:0;top:21px;width:729px;text-align:center;font-family:"Questrial",sans-serif;font-weight:400;font-size:21px;color:var(--blue)}
.solutions h2 span{color:var(--teal)}
.cards{position:absolute;left:44px;top:68px;display:flex;gap:7px}
.card{position:relative;width:154px;height:215px;transform:skewX(-9deg);overflow:hidden}
.card .photo{position:absolute;inset:0}
.card .label{position:absolute;left:0;right:0;top:159px;height:36px;background:var(--label-bg);opacity:.95;display:flex;align-items:center;justify-content:center}
.card .label span{transform:skewX(9deg);font-family:"Raleway",sans-serif;font-weight:600;font-size:9.6px;color:var(--blue);text-align:center;line-height:13px}
.p1{background:linear-gradient(160deg,#6e5a3c,#a89a78 45%,#3d4f70)}
.p2{background:linear-gradient(160deg,#e9e9e6,#9ea4a8 50%,#3d4c8c)}
.p3{background:linear-gradient(180deg,#4e8fd0,#8fb7e0 45%,#8b7d6a)}
.p4{background:linear-gradient(180deg,#a9c6e2,#7e9a7c 40%,#5b7f96)}

.oxidation{position:absolute;left:0;top:956px;width:729px;height:202px;background:var(--teal);color:var(--white);text-align:center;font-family:"Open Sans",sans-serif}
.oxidation h2{margin-top:23px;font-family:"Raleway",sans-serif;font-weight:500;font-size:21px}
.oxidation .lead{margin-top:16px;font-size:8.2px}
.oxidation ul{list-style:none;margin-top:10px;font-size:8.2px;line-height:17px}
.oxidation li::before{content:"";display:inline-block;border-left:3px solid #fff;border-top:3px solid transparent;border-bottom:3px solid transparent;margin-right:7px}
.oxidation .close{margin-top:11px;font-size:8.2px;line-height:17.5px}

.footer{position:absolute;left:0;top:1158px;width:729px;height:42px;background:var(--white)}
.footer .copy{position:absolute;left:28px;top:17px;font-size:7px;color:#333}
.footer .social{position:absolute;left:594px;top:19px;display:flex;gap:13px}
.footer .social i{display:block;width:8px;height:8px;border-radius:50%;background:#3a3a3a}
.footer .social i:first-child{background:var(--blue)}
</style>
</head>
<body>

<header class="hero">
  <div class="hero-photo" role="img" aria-label="Dusk view of an industrial plant with chimneys and cooling tower"></div>
  <div class="hero-top">
    <div class="email">Email id : info@velmirlab.net</div>
    <div class="phone">Call Us : 123-456-7890</div>
    <div class="brand"><div class="dot"></div><div class="name">VelmirLab</div></div>
  </div>
  <nav class="nav">
    <a class="home" href="#">HOME</a>
    <a class="about" href="#">ABOUT US</a>
    <a class="tech" href="#">TECHNOLOGY</a>
    <a class="prod" href="#">PRODUCTS</a>
    <a class="contact" href="#">CONTACT US</a>
  </nav>
  <h1 class="hero-title">Advanced Oxidation Science<br>for Environmental Pollution<br>Management</h1>
  <div class="hero-sub">Duis Aute Lrure Dolor in Reprehenderit in Voluptate</div>
  <a class="btn" href="#">Read More</a>
  <div class="slider-ctrl">
    <svg width="6" height="9" viewBox="0 0 6 9"><path d="M5 1 1.5 4.5 5 8" fill="none" stroke="#222" stroke-width="1.3"/></svg>
    <svg width="6" height="9" viewBox="0 0 6 9"><path d="M1 1 4.5 4.5 1 8" fill="none" stroke="#222" stroke-width="1.3"/></svg>
  </div>
</header>

<section class="welcome">
  <div class="rule l"></div><div class="rule r"></div>
  <h2>Welcome to <span>VelmirLab</span></h2>
  <p>Lorem ipsum dolor sit amet, consectetur adipiscing elit, sed do eiusmod tempor incididunt ut labore et dolore magna aliqua. Ut enim ad minim veniam, quis nostrud exercitation ullamco laboris nisi ut aliquip ex ea commodo consequat. Duis aute irure dolor in reprehenderit in voluptate velit esse cillum dolore eu fugiat nulla pariatur. Excepteur sint occaecat cupidatat non proident, sunt in culpa qui officia deserunt mollit anim id est laborum.</p>
  <a class="btn" href="#">Read More</a>
</section>

<section class="solutions">
  <h2>Sol<span>utions</span></h2>
  <div class="cards">
    <div class="card"><div class="photo p1" role="img" aria-label="Refinery piping and desulfurization equipment"></div><div class="label"><span>Fuel Oil Desulfurization</span></div></div>
    <div class="card"><div class="photo p2" role="img" aria-label="Gloved hand loading vials into a laboratory analyzer"></div><div class="label"><span>Volatile Organic Compunds<br>(VOC)</span></div></div>
    <div class="card"><div class="photo p3" role="img" aria-label="Industrial stack emitting steam against blue sky"></div><div class="label"><span>Flue Gas Scrubbing</span></div></div>
    <div class="card"><div class="photo p4" role="img" aria-label="Circular clarifier tanks at a wastewater treatment plant"></div><div class="label"><span>Wastewater Treatment</span></div></div>
  </div>
</section>

<section class="oxidation">
  <h2>Advanced Oxidation</h2>
  <p class="lead">Advanced Oxidation refers to a &nbsp;variety of techniques employing the Hydroxyl Radical, an energetic, highly reactive cousin of the water molecule</p>
  <ul>
    <li>To add oxygen to inorganic molecules</li>
    <li>To remove hydrogen from organic molecule</li>
  </ul>
  <p class="close">These transformations convert important industrial contaminants into reactive forms that can be captured or<br>that disintegrate into harmless end products.</p>
</section>

<footer class="footer">
  <div class="copy">All Rights Reserved. Copyrights @company Name. 2016</div>
  <div class="social"><i></i><i></i><i></i><i></i><i></i></div>
</footer>

</body>
</html>
```